Turning Lecture Halls into Studios of Bold Discovery

This is for a book cover aimed at professors in higher education who want to infuse creative thinking into their classroom. It should have the title on the cover (see name of project). Our first idea is to have a stack of academic type books on a desk in black and white and then have a colorful rainbow light thread hitting the books. However, we are open to options! It has to be sophisticated, cool, and creative ;)

Target Market(s)

Higher Education Instructors

Industry/Entity Type

education

Font styles to use
Serif
Sans Serif

Requirements
Nice to have
• a creative feel of some sort
Should not have
• lightbulbs

```html
<!DOCTYPE html>
<html lang="en">
<head>
<meta charset="utf-8">
<title>Turning Lecture Halls into Studios of Bold Discovery</title>
<link rel="stylesheet" href="https://fonts.googleapis.com/css2?family=Anton&display=swap">
<style>
  :root {
    --page: #ffffff;
    --cover-cream: #fbf7e6;
    --cover-cream-deep: #f3eedb;
    --ink: #231f20;
    --accent-red: #c92336;
  }
  html, body {
    margin: 0;
    padding: 0;
    width: 1200px;
    height: 1200px;
    overflow: hidden;
    background: var(--page);
  }
  .canvas {
    position: relative;
    width: 1200px;
    height: 1200px;
  }
  .book-cover {
    position: absolute;
    left: 204px;
    top: 50px;
    width: 792px;
    height: 1100px;
    display: block;
  }
  .cover-title {
    font-family: "Anton", "Arial Narrow", sans-serif;
    fill: var(--ink);
  }
  .cover-title .title-accent { fill: var(--accent-red); }
</style>
</head>
<body>
<main class="canvas">
  <svg class="book-cover" viewBox="0 0 1088 1510" xmlns="http://www.w3.org/2000/svg">
    <defs>
      <linearGradient id="cover-paper" x1="0" y1="0" x2="0" y2="1">
        <stop offset="0" stop-color="var(--cover-cream)"/>
        <stop offset="1" stop-color="var(--cover-cream-deep)"/>
      </linearGradient>
      <linearGradient id="artwork-tones" x1="0" y1="0" x2="1" y2="0">
        <stop offset="0" stop-color="var(--ink)"/>
        <stop offset="0.55" stop-color="var(--accent-red)"/>
        <stop offset="1" stop-color="var(--ink)"/>
      </linearGradient>
    </defs>

    <rect class="cover-background" x="0" y="0" width="1088" height="1510" fill="url(#cover-paper)"/>

    <rect class="cover-artwork" x="66" y="522" width="571" height="988" fill="url(#artwork-tones)"
          role="img" aria-label="Illustration area: tall leaning book spines in black and red with two seated student silhouettes on top"/>

    <g class="cover-title">
      <text x="204" y="290" font-size="190" textLength="380" lengthAdjust="spacingAndGlyphs">TURNING</text>
      <text class="title-accent" x="621" y="290" font-size="190" textLength="380" lengthAdjust="spacingAndGlyphs">LECTURE</text>
      <text x="1001" y="396" font-size="95" text-anchor="end" textLength="118" lengthAdjust="spacingAndGlyphs">HALLS</text>
      <text x="1001" y="497" font-size="95" text-anchor="end" textLength="92" lengthAdjust="spacingAndGlyphs">INTO</text>
      <text x="1001" y="602" font-size="95" text-anchor="end" textLength="162" lengthAdjust="spacingAndGlyphs">STUDIOS</text>
      <text x="1001" y="705" font-size="95" text-anchor="end" textLength="50" lengthAdjust="spacingAndGlyphs">OF</text>
      <text x="1001" y="810" font-size="95" text-anchor="end" textLength="96" lengthAdjust="spacingAndGlyphs">BOLD</text>
      <text x="1001" y="914" font-size="95" text-anchor="end" textLength="210" lengthAdjust="spacingAndGlyphs">DISCOVERY</text>
    </g>
  </svg>
</main>
</body>
</html>
```